Larchly Business Cards

Create new business cards with the details below.

Trevor Halse
Director

MB: +61 417 352 940
PH: 1300 514 637
Email: trevor.halse@larchly-example.com.au
Address: 27A Pemberly Lane, Harrowmere VIC 3094 Australia
Website: www.larchly-example.com.au

Requirements
Must have
• must be clean looking

```html
<!DOCTYPE html>
<html lang="en">
<head>
<meta charset="utf-8">
<title>Larchly Business Cards</title>
<link rel="stylesheet" href="https://fonts.googleapis.com/css2?family=Montserrat:wght@400;500;700;800&display=swap">
<style>
  :root {
    --stage: #232323;
    --card-white: #ffffff;
    --lime: #a8d130;
    --lime-light: #b8dc40;
    --charcoal: #333333;
    --ink: #2a2a2a;
    --ink-soft: #444444;
  }
  * { box-sizing: border-box; margin: 0; padding: 0; }
  html, body {
    width: 1200px;
    height: 1000px;
    overflow: hidden;
    background: var(--stage);
    font-family: "Montserrat", sans-serif;
  }
  .stage { position: relative; width: 1200px; height: 1000px; }

  .card {
    position: absolute;
    width: 640px;
    height: 366px;
    border-radius: 34px;
    overflow: hidden;
    background: var(--card-white);
  }
  .card-contact { left: 420px; top: 70px; }
  .card-brand { left: 140px; top: 540px; background: var(--charcoal); }

  .card-shapes { position: absolute; inset: 0; width: 100%; height: 100%; }
  .shape-lime { fill: var(--lime); }
  .shape-lime-light { fill: var(--lime-light); }
  .shape-charcoal { fill: var(--charcoal); }
  .shape-white { fill: var(--card-white); }

  .brand {
    position: absolute;
    display: flex;
    align-items: center;
    gap: 10px;
  }
  .brand-square {
    width: 22px;
    height: 22px;
    background: var(--charcoal);
  }
  .brand-name {
    font-weight: 800;
    color: var(--charcoal);
    letter-spacing: 1px;
    text-transform: uppercase;
    line-height: 1;
  }

  .card-contact .brand { left: 44px; top: 60px; }
  .card-contact .brand-name { font-size: 30px; }

  .person { position: absolute; left: 110px; top: 150px; text-align: right; width: 220px; }
  .person-name { font-size: 27px; font-weight: 500; color: var(--ink); }
  .person-role { font-size: 17px; font-weight: 500; color: var(--lime); margin-top: 2px; }
  .person-email {
    position: absolute; left: 40px; top: 222px; width: 360px;
    font-size: 12px; color: var(--ink-soft); text-align: center;
  }

  .details {
    position: absolute; left: 440px; top: 58px;
    font-size: 12.5px; line-height: 1.45; color: var(--ink);
  }
  .details .address { margin-top: 12px; }

  .card-brand .brand { left: 190px; top: 158px; }
  .card-brand .brand-name { font-size: 44px; }
  .card-brand .brand-square { width: 34px; height: 34px; background: var(--lime); }
  .website {
    position: absolute; left: 170px; top: 282px; width: 320px;
    font-size: 16px; font-weight: 500; color: var(--ink); text-align: center;
  }
</style>
</head>
<body>
<main class="stage">

  <section class="card card-contact" aria-label="Contact side">
    <svg class="card-shapes" viewBox="0 0 640 366" aria-hidden="true">
      <polygon class="shape-lime-light" points="390,0 640,0 640,232 300,148"/>
      <polygon class="shape-charcoal" points="466,189 640,232 640,366 420,366"/>
    </svg>
    <div class="brand">
      <span class="brand-square"></span>
      <span class="brand-name">Larchly</span>
    </div>
    <div class="person">
      <p class="person-name">Trevor Halse</p>
      <p class="person-role">Director</p>
    </div>
    <p class="person-email">trevor.halse@larchly-example.com.au</p>
    <div class="details">
      <p>MB:&nbsp; +61 417 352 940</p>
      <p>PH:&nbsp;&nbsp; 1300 514 637</p>
      <p class="address">27A Pemberly Lane,<br>Harrowmere VIC 3094<br>Australia</p>
    </div>
  </section>

  <section class="card card-brand" aria-label="Brand side">
    <svg class="card-shapes" viewBox="0 0 640 366" aria-hidden="true">
      <polygon class="shape-white" points="180,0 548,0 470,366 80,366"/>
      <polygon class="shape-lime" points="0,192 170,262 62,366 0,366"/>
      <polygon class="shape-lime-light" points="548,0 640,0 640,130 520,90"/>
      <polygon class="shape-charcoal" points="520,90 640,130 640,366 470,366"/>
    </svg>
    <div class="brand">
      <span class="brand-square"></span>
      <span class="brand-name">Larchly</span>
    </div>
    <p class="website">www.larchly-example.com.au</p>
  </section>

</main>
</body>
</html>
```